Tidewell Care Group Site Re-Design

Review content of current website www.tidewellcaregroup.example and re-design each page - I have attached a comprehensive website brief which outlines the products and services that tidewell care group sells online, the type of style I like my website to be in which is clean, uncluttered, professional and modern, it also indicates which other websites that I admire and that I would like my existing site to be changed to that style. The Personal Trainer Development Sub Page is going to be re -written and I am hoping that the new design will make my site more modern and provide a better user experience. I would also be open if the designer wanted to use their creative talents to re-design my logo if you think you could do a better job. I look forward to seeing some awesome designs.

Target Market(s)

Refer to attached design brief

Industry/Entity Type

Health And Wellness

Number of Pages Required

5+ page

Colors
9bcb3c
6b449b

Requirements
Must have
• Refer to design brief
Nice to have
• Refer to design brief
Should not have
• Refer to design brief

```html
<!DOCTYPE html>
<html lang="en">
<head>
<meta charset="utf-8">
<title>Tidewell Care Group</title>
<link rel="stylesheet" href="https://fonts.googleapis.com/css2?family=Barlow+Condensed:wght@400;500;600;700&family=Lora:wght@400;700&family=Montserrat:wght@400;600;700&display=swap">
<style>
:root{
  --green:#9bcb3c;
  --green-dark:#7fae22;
  --green-deeper:#6a9818;
  --green-deepest:#5a8513;
  --purple:#6b449b;
  --ink:#1f1f1f;
  --ink-soft:#262626;
  --charcoal:#2b2b2b;
  --white:#ffffff;
  --grey:#8a8a8a;
  --line:#3b3b3b;
}
*{margin:0;padding:0;box-sizing:border-box}
html,body{width:1200px;height:4749px;overflow:hidden}
body{font-family:'Lora',Georgia,serif;color:var(--ink);background:var(--white);position:relative}
.heading{font-family:'Barlow Condensed','Arial Narrow',sans-serif;letter-spacing:3px;text-transform:uppercase}
.ui{font-family:'Montserrat',Arial,sans-serif}
section,header,footer{position:absolute;left:0;width:1200px}

/* top bar + hero */
.hero{top:0;height:690px;background:linear-gradient(160deg,#4a4442 0%,#2e2a29 45%,#1c1a1a 100%);overflow:hidden}
.hero-photo{position:absolute;inset:0;background:radial-gradient(ellipse at 50% 30%,rgba(120,110,105,.55),rgba(20,18,18,0) 60%)}
.topbar{position:absolute;top:0;left:0;width:1200px;height:44px;background:rgba(20,20,20,.85);color:#ddd;font-size:12px;display:flex;align-items:center}
.topbar .item{position:absolute;display:flex;align-items:center;gap:8px}
.topbar svg{display:block}
.social{position:absolute;display:flex;gap:14px}
.social span{width:11px;height:11px;border-radius:50%;background:currentColor;display:block}
.brand{position:absolute;left:118px;top:104px;font-family:'Montserrat',Arial,sans-serif;font-weight:700;font-size:24px;letter-spacing:2px;color:var(--green)}
.nav{position:absolute;top:116px;right:150px;display:flex;gap:38px;font-size:11px;font-weight:600;letter-spacing:1px;color:#ddd}
.nav .active{color:#fff}
.search{position:absolute;top:112px;right:110px}
.hero-title{position:absolute;top:282px;width:100%;text-align:center;color:#fff}
.hero-title .l1{font-weight:700;font-size:96px;letter-spacing:10px;line-height:1}
.hero-title .l2{font-weight:400;font-size:84px;letter-spacing:10px;line-height:1;margin-top:22px}
.hero-sub{position:absolute;top:548px;width:100%;text-align:center;color:#bbb;font-size:14px;letter-spacing:1px}
.dots{position:absolute;top:644px;left:596px;display:flex;gap:10px;align-items:center}
.dots span{width:10px;height:10px;border-radius:50%;background:#888}
.dots .on{background:transparent;border:2px solid #fff;width:14px;height:14px}

/* promos */
.promos{top:690px;height:330px}
.promo-green{position:absolute;left:0;top:0;width:617px;height:330px;background:var(--green);color:#fff;padding:50px 50px}
.promo-dark{position:absolute;left:617px;top:0;width:583px;height:330px;background:linear-gradient(90deg,#262626 0%,#2a2a2a 55%,#5a4f4a 100%);color:#fff;padding:60px 62px}
.promo-title{font-size:38px;font-weight:700}
.promo-text{font-size:12px;line-height:1.6;margin-top:18px;max-width:480px;color:#f2f2f2}
.signup{position:absolute;right:70px;bottom:52px;font-size:26px;font-weight:600;letter-spacing:4px;color:#d7ef9f}
.btn-outline{position:absolute;left:62px;bottom:50px;border:2px solid #fff;padding:12px 18px;font-size:10px;font-weight:700;letter-spacing:1px}

/* features */
.features{top:1020px;height:626px;text-align:center}
.section-title{font-size:34px;font-weight:600;letter-spacing:5px}
.features .section-title{position:absolute;top:95px;width:100%}
.features .lead{position:absolute;top:170px;left:330px;width:540px;font-size:12px;line-height:1.7;color:#444}
.divider{position:absolute;left:500px;width:200px;height:10px}
.feature-photos{position:absolute;top:332px;left:136px;display:flex;gap:25px}
.feature-photos div{width:304px;height:190px}

/* schedule */
.schedule{top:1646px;height:228px;background:var(--charcoal);color:#fff;display:flex}
.day{width:240px;height:228px;border-right:1px solid var(--line);padding:52px 0 0 82px;font-size:11px;font-family:'Montserrat',Arial,sans-serif}
.day:first-child{padding-left:82px}
.day:last-child{border-right:none}
.day h4{font-weight:700;letter-spacing:1px;margin-bottom:30px}
.day p{line-height:1.6;letter-spacing:1px;margin-bottom:22px;color:#e8e8e8}

/* yoga */
.yoga{top:1874px;height:557px;background:#fff}
.yoga-photo{position:absolute;left:50px;top:35px;width:740px;height:490px;background:radial-gradient(ellipse at 45% 55%,#dcdcdc 0%,#f4f4f4 55%,#fff 75%)}
.yoga-copy{position:absolute;right:80px;top:262px;text-align:right}
.yoga-copy .l1{font-size:62px;font-weight:600;letter-spacing:5px;line-height:1}
.yoga-copy .l2{font-size:80px;font-weight:600;letter-spacing:5px;color:var(--purple);line-height:1;margin-top:8px}
.yoga-copy p{font-size:12px;color:#777;margin-top:14px}

/* courses */
.courses{top:2431px;height:396px;background:var(--charcoal);color:#fff}
.courses .section-title{position:absolute;top:70px;width:100%;text-align:center;color:#fff}
.courses .sub{position:absolute;top:124px;width:100%;text-align:center;font-size:11px;color:#bbb}
.arrows{position:absolute;top:80px;left:1090px;display:flex;gap:14px}
.arrows span{width:50px;height:50px;border-radius:50%;background:var(--green);display:flex;align-items:center;justify-content:center}
.course-strip{position:absolute;top:190px;left:0;display:flex}
.course-strip div{width:300px;height:206px}

/* diet */
.diet{top:2827px;height:497px;background:var(--charcoal);color:#fff}
.perks{position:absolute;left:0;top:0;width:412px;height:497px}
.perk{height:165px;padding:42px 0 0 56px;font-family:'Montserrat',Arial,sans-serif}
.perk:nth-child(1){background:var(--green-dark)}
.perk:nth-child(2){background:var(--green-deeper)}
.perk:nth-child(3){background:var(--green-deepest);height:167px;border-bottom:6px solid var(--green)}
.perk-head{display:flex;align-items:center;gap:22px;font-size:11px;font-weight:700;letter-spacing:1px}
.perk p{margin:14px 0 0 46px;font-size:9px;line-height:1.8;letter-spacing:1px;font-weight:600;color:#e9f5cf;max-width:260px}
.diet-title{position:absolute;left:484px;top:90px;font-size:58px;font-weight:600;letter-spacing:6px}
.diet-text{position:absolute;left:488px;width:590px;font-size:10px;line-height:1.9;color:#cfcfcf;letter-spacing:.5px}

/* trainer */
.trainer{top:3324px;height:776px;text-align:center}
.trainer .section-title{position:absolute;top:70px;width:100%;font-size:54px}
.trainer .sub{position:absolute;top:156px;width:100%;font-size:12px;letter-spacing:1px;color:#999}
.trainer-photo{position:absolute;left:136px;top:212px;width:963px;height:364px;background:radial-gradient(ellipse at 50% 45%,#3d4a66 0%,#1a2030 35%,#07090d 70%)}
.trainer-name{position:absolute;top:621px;width:100%;font-family:'Montserrat',Arial,sans-serif;font-size:12px;font-weight:700;letter-spacing:1px}
.trainer .social{left:566px;top:692px;color:#333}

/* testimonial */
.testimonial{top:4100px;height:563px;background:linear-gradient(100deg,#1e1618 0%,#3a2a30 35%,#4a2f3b 60%,#2a2226 100%);color:#fff;text-align:center}
.testimonial .section-title{position:absolute;top:108px;width:100%;font-size:40px}
.quote{position:absolute;top:200px;left:300px;width:600px;font-size:17px;line-height:1.75}
.quote-mark{position:absolute;top:312px;left:586px;font-size:56px;font-weight:700;line-height:1}
.author{position:absolute;top:380px;left:548px;display:flex;align-items:center;gap:16px}
.avatar{width:54px;height:54px;border-radius:50%;background:#b88a8a;border:3px solid #fff}
.author span{font-family:'Montserrat',Arial,sans-serif;font-size:11px;font-weight:700;letter-spacing:1px}
.t-arrow{position:absolute;top:268px;width:56px;height:56px;border-radius:50%;border:2px solid #fff;display:flex;align-items:center;justify-content:center}

footer{top:4663px;height:86px;background:var(--ink-soft);color:#888;text-align:center;font-size:10px;letter-spacing:2px;line-height:86px;font-family:'Montserrat',Arial,sans-serif;text-transform:uppercase}
</style>
</head>
<body>

<header class="hero">
  <div class="hero-photo" role="img" aria-label="Athlete gripping a barbell in a dim gym"></div>
  <div class="topbar ui">
    <div class="item" style="left:140px">
      <svg width="12" height="12" viewBox="0 0 12 12"><path d="M2 1h3l1 3-2 1a7 7 0 0 0 3 3l1-2 3 1v3c0 .6-.4 1-1 1A10 10 0 0 1 1 2c0-.6.4-1 1-1z" fill="#9bcb3c"/></svg>
      020.5550198734
    </div>
    <div class="item" style="left:460px">
      <svg width="12" height="12" viewBox="0 0 12 12"><path d="M1 5l10-4-4 10-1-5z" fill="#9bcb3c"/></svg>
      42 Harbour Lane QLD, 4000
    </div>
    <div class="social" style="left:952px;top:17px;color:#ddd"><span></span><span></span><span></span><span></span><span></span></div>
  </div>
  <div class="brand">TIDEWELL</div>
  <nav class="nav ui"><span class="active">HOME</span><span>WORKS</span><span>BLOG</span><span>ABOUT</span></nav>
  <svg class="search" width="16" height="16" viewBox="0 0 16 16"><circle cx="6.5" cy="6.5" r="4.5" fill="none" stroke="#ddd" stroke-width="2"/><path d="M10 10l4 4" stroke="#ddd" stroke-width="2"/></svg>
  <div class="hero-title heading"><div class="l1">Champions</div><div class="l2">Work Harder</div></div>
  <div class="hero-sub">Prepare yourself towards a healthy lifestyle</div>
  <div class="dots"><span></span><span class="on"></span></div>
</header>

<section class="promos">
  <div class="promo-green">
    <div class="promo-title heading">90 Day Challenge</div>
    <p class="promo-text">Lorem ipsum dolor sit amet, consectetur adipiscing elit, sed do eiusmod tempor incididunt ut labore et dolore magna aliqua. Ut enim ad minim veniam, quis nostrud exercitation ullamco laboris nisi ut aliquip ex ea commodo consequat.</p>
    <div class="signup heading">Sign Up</div>
  </div>
  <div class="promo-dark" role="img" aria-label="Athlete resting between sets">
    <div class="promo-title heading">Train.Sleep.Repeat</div>
    <p class="promo-text" style="max-width:380px">Lorem ipsum dolor sit amet, consectetur adipiscing elit, sed do eiusmod tempor incididunt ut labore et dolore magna aliqua. Ut enim ad minim veniam, quis nostrud exercitation ullamco laboris nisi.</p>
    <div class="btn-outline ui">LEARN MORE</div>
  </div>
</section>

<section class="features">
  <h2 class="section-title heading">What Makes Us Different</h2>
  <p class="lead">Lorem ipsum dolor sit amet, consectetur adipiscing elit, sed do eiusmod tempor incididunt ut labore et dolore magna aliqua. Ut enim ad minim veniam, quis nostrud exercitation ullamco laboris nisi ut.</p>
  <svg class="divider" style="top:272px" viewBox="0 0 200 10"><line x1="0" y1="5" x2="80" y2="5" stroke="#6b449b" stroke-width="2"/><circle cx="90" cy="5" r="2.5" fill="#6b449b"/><circle cx="100" cy="5" r="2.5" fill="#6b449b"/><circle cx="110" cy="5" r="2.5" fill="#6b449b"/><line x1="120" y1="5" x2="200" y2="5" stroke="#6b449b" stroke-width="2"/></svg>
  <div class="feature-photos">
    <div role="img" aria-label="Barbell training session" style="background:linear-gradient(135deg,#2a2f38,#5a5f66 60%,#1a1d22)"></div>
    <div role="img" aria-label="Group fitness class" style="background:linear-gradient(135deg,#8a5a2e,#c98a4a 50%,#5a3a22)"></div>
    <div role="img" aria-label="Smiling personal trainer" style="background:linear-gradient(135deg,#b9cde6,#d8e4f2 60%,#a7bcd8)"></div>
  </div>
  <svg class="divider" style="top:557px" viewBox="0 0 200 10"><line x1="0" y1="5" x2="80" y2="5" stroke="#6b449b" stroke-width="2"/><circle cx="90" cy="5" r="2.5" fill="#6b449b"/><circle cx="100" cy="5" r="2.5" fill="#6b449b"/><circle cx="110" cy="5" r="2.5" fill="#6b449b"/><line x1="120" y1="5" x2="200" y2="5" stroke="#6b449b" stroke-width="2"/></svg>
</section>

<section class="schedule">
  <div class="day"><h4>MONDAY</h4><p>CLASS NAME<br>TIME | FULL</p><p>CLASS NAME<br>TIME | FULL</p></div>
  <div class="day"><h4>TUESDAY</h4><p>CLASS NAME<br>TIME | FULL</p><p>CLASS NAME<br>TIME | FULL</p></div>
  <div class="day"><h4>WEDNESDAY</h4><p>CLASS NAME<br>TIME | FULL</p><p>CLASS NAME<br>TIME | FULL</p></div>
  <div class="day"><h4>THURSDAY</h4><p>CLASS NAME<br>TIME | FULL</p><p>CLASS NAME<br>TIME | FULL</p></div>
  <div class="day"><h4>FRIDAY</h4><p>CLASS NAME<br>TIME | FULL</p><p>CLASS NAME<br>TIME | FULL</p></div>
</section>

<section class="yoga">
  <div class="yoga-photo" role="img" aria-label="Woman stretching in a seated yoga pose"></div>
  <div class="yoga-copy heading">
    <div class="l1">Try Our</div>
    <div class="l2">Yoga Classes</div>
    <p style="font-family:'Lora',serif;text-transform:none;letter-spacing:0">Lorem ipsum dolor sit amet, consectetur</p>
  </div>
</section>

<section class="courses">
  <h2 class="section-title heading">Opening Courses</h2>
  <div class="sub">New Courses</div>
  <div class="arrows">
    <span><svg width="14" height="14" viewBox="0 0 14 14"><path d="M9 2L4 7l5 5" fill="none" stroke="#fff" stroke-width="2"/></svg></span>
    <span><svg width="14" height="14" viewBox="0 0 14 14"><path d="M5 2l5 5-5 5" fill="none" stroke="#fff" stroke-width="2"/></svg></span>
  </div>
  <div class="course-strip">
    <div role="img" aria-label="Kettlebell class" style="background:linear-gradient(135deg,#3a3f4a,#6a6f7a 50%,#23262d)"></div>
    <div role="img" aria-label="Trainer coaching a client" style="background:linear-gradient(135deg,#6a5a52,#a89888 50%,#3a3230)"></div>
    <div role="img" aria-label="Stretching on a gym floor" style="background:linear-gradient(135deg,#5a6f8a,#9aaabb 50%,#3a4a5e)"></div>
    <div role="img" aria-label="Cardio machines in a studio" style="background:linear-gradient(135deg,#22324a,#4a5e7a 50%,#141e2c)"></div>
  </div>
</section>

<section class="diet">
  <div class="perks">
    <div class="perk">
      <div class="perk-head"><svg width="22" height="22" viewBox="0 0 22 22"><circle cx="11" cy="11" r="9" fill="none" stroke="#fff" stroke-width="2"/><path d="M11 6v5l3 2" stroke="#fff" stroke-width="2" fill="none"/></svg>YOUR SCHEDULE</div>
      <p>SED UT PERSPICIATIS UNDE OMNIS ISTE NATUS ERROR SIT VOLUPTATEM</p>
    </div>
    <div class="perk">
      <div class="perk-head"><svg width="22" height="22" viewBox="0 0 22 22"><path d="M3 4h16v10H9l-4 4v-4H3z" fill="none" stroke="#fff" stroke-width="2"/></svg>YOUR COMMUNITY</div>
      <p>SED UT PERSPICIATIS UNDE OMNIS ISTE NATUS ERROR SIT VOLUPTATEM</p>
    </div>
    <div class="perk">
      <div class="perk-head"><svg width="22" height="22" viewBox="0 0 22 22"><circle cx="11" cy="11" r="9" fill="none" stroke="#fff" stroke-width="2"/><path d="M11 11V2A9 9 0 0 1 20 11z" fill="#fff"/></svg>YOUR PACE</div>
      <p>SED UT PERSPICIATIS UNDE OMNIS ISTE NATUS ERROR SIT VOLUPTATEM</p>
    </div>
  </div>
  <h2 class="diet-title heading">Healthy Diet</h2>
  <p class="diet-text" style="top:220px">SED UT PERSPICIATIS UNDE OMNIS ISTE NATUS ERROR SIT VOLUPTATEM ACCUSANTIUM DOLOREMQUE LAUDANTIUM, TOTAM REM APERIAM, EAQUE IPSA QUAE AB ILLO INVENTORE VERITATIS ET QUASI ARCHITECTO BEATAE VITAE DICTA SUNT EXPLICABO. NEMO ENIM IPSAM VOLUPTATEM QUIA VOLUPTAS SIT ASPERNATUR AUT ODIT AUT FUGIT, SED QUIA.</p>
  <p class="diet-text" style="top:345px">CONSEQUUNTUR MAGNI DOLORES EOS QUI RATIONE VOLUPTATEM SEQUI NESCIUNT. NEQUE PORRO QUISQUAM EST, QUI DOLOREM IPSUM QUIA DOLOR SIT AMET, CONSECTETUR, ADIPISCI VELIT, SED QUIA NON NUMQUAM EIUS MODI TEMPORA INCIDUNT UT LABORE ET DOLORE.</p>
</section>

<section class="trainer">
  <h2 class="section-title heading">Meet Your Trainer</h2>
  <div class="sub">LOREM IPSUM DOLOR SIT AMET, CONSECTETUR ADIPISCING ELIT, SED DO EIUSMOD TEMPOR INCIDIDUNT UT</div>
  <div class="trainer-photo" role="img" aria-label="Portrait of personal trainer Marcus Hale"></div>
  <div class="trainer-name">MARCUS HALE</div>
  <div class="social"><span></span><span></span><span></span><span></span></div>
</section>

<section class="testimonial" role="img" aria-label="Gym interior with dumbbell racks and exercise bikes">
  <h2 class="section-title heading">Testimonial</h2>
  <p class="quote">Lorem ipsum dolor sit amet, consectetur adipiscing elit, sed do eiusmod tempor incididunt ut labore et dolore magna aliqua. Ut enim ad minim veniam, quis nostrud</p>
  <div class="quote-mark">&ldquo;</div>
  <div class="author"><div class="avatar"></div><span>DANA REYES</span></div>
  <div class="t-arrow" style="left:30px"><svg width="14" height="14" viewBox="0 0 14 14"><path d="M9 2L4 7l5 5" fill="none" stroke="#fff" stroke-width="2"/></svg></div>
  <div class="t-arrow" style="right:30px"><svg width="14" height="14" viewBox="0 0 14 14"><path d="M5 2l5 5-5 5" fill="none" stroke="#fff" stroke-width="2"/></svg></div>
</section>

<footer>Copyright 2016 by tidewell care group</footer>

</body>
</html>
```